Infectious Diseases Research Laboratory Needs Business Card

We need a business card for an academic research laboratory based in Kansas City called MORVEK. The full lab name is Microbial Dose-Response/Exposure Bridging Studies Laboratory, but this does not need to be incorporated. We study novel ways to optimize the treatment of multidrug-resistant bacterial infections ("superbugs") throughout the entire biomedical research spectrum (from benchtop to bedside). The name MORVEK is not only an acronym for our lab name, but also represents our desire to make discoveries and explore the unknown (the stars, if you well). It also serves as an ode to the state of Kansas motto where we are based, ad astra per aspera ("to the stars, through difficulty").

Target Market(s)

Pharmaceutical companies, researchers

Industry/Entity Type

Pharmaceutical

Contact Information for Business Card

The business card should incorporate and complement our new logo (see uploaded files). Double-sided designs are preferred. Looking for something modern, but professional.

Font styles to use
Sans Serif

Requirements
Must have
• Double-sided. One side would ideally be a solid color incorporating logo and the other should also have the logo (smaller), but incorporate staff information.
• Color codes:
• Red: #F04C51
• Blue: #3477B5
• Gray: #808285

```html
<!DOCTYPE html>
<html lang="en">
<head>
<meta charset="utf-8">
<title>MORVEK Business Card</title>
<link href="https://fonts.googleapis.com/css2?family=Roboto:wght@300;400;500&display=swap" rel="stylesheet">
<style>
  :root {
    --red: #F04C51;
    --blue: #3477B5;
    --blue-dark: #1f5a8f;
    --gray: #808285;
    --ink: #1c1c1c;
    --white: #ffffff;
    --backdrop: #d3e6ec;
  }
  * { box-sizing: border-box; margin: 0; padding: 0; }
  html, body { width: 1200px; height: 900px; overflow: hidden; }
  body {
    background: var(--backdrop);
    font-family: "Roboto", Arial, sans-serif;
    position: relative;
  }
  .card {
    position: absolute;
    width: 620px;
    height: 354px;
    border-radius: 18px;
    overflow: hidden;
    box-shadow: 0 10px 24px rgba(0,0,0,0.18);
  }
  /* Front side */
  .card-front {
    left: 110px; top: 56px;
    background: var(--red);
  }
  .front-brand {
    position: absolute;
    left: 0; right: 0; top: 128px;
    display: flex; align-items: center; justify-content: center; gap: 22px;
  }
  .brand-dot {
    width: 62px; height: 62px; border-radius: 50%;
    background: var(--white);
  }
  .front-brand .brand-name {
    color: var(--white);
    font-size: 68px; font-weight: 300; letter-spacing: 6px;
  }
  .front-web {
    position: absolute; left: 0; right: 0; bottom: 44px;
    text-align: center; color: var(--white);
    font-size: 15px; letter-spacing: 0.5px;
  }
  /* Back side */
  .card-back {
    left: 470px; top: 486px;
    background: var(--white);
  }
  .back-panel { position: absolute; inset: 0; }
  .back-brand {
    position: absolute; left: 40px; top: 44px;
  }
  .back-brand-row { display: flex; align-items: center; gap: 12px; }
  .back-brand .brand-dot { width: 38px; height: 38px; background: var(--blue); }
  .back-brand .brand-name {
    color: var(--red); font-size: 40px; font-weight: 300; letter-spacing: 4px;
  }
  .lab-name {
    margin-top: 4px; padding-top: 3px;
    border-top: 1px solid var(--gray);
    width: 210px;
    color: var(--gray); font-size: 6.5px; line-height: 1.35; letter-spacing: 0.3px;
    text-transform: uppercase;
  }
  .contact-list {
    position: absolute; left: 40px; bottom: 34px;
    list-style: none;
  }
  .contact-list li {
    display: flex; align-items: center; gap: 12px;
    font-size: 15px; color: var(--ink); height: 28px;
  }
  .contact-icon {
    width: 22px; height: 22px; background: var(--blue);
    display: flex; align-items: center; justify-content: center;
  }
  .name-ribbon {
    position: absolute; left: 318px; top: 38px;
    width: 302px; height: 58px;
    background: var(--blue);
    color: var(--white);
    display: flex; flex-direction: column; justify-content: center;
    padding-left: 40px;
  }
  .person-name { font-size: 21px; font-weight: 400; }
  .person-role { font-size: 12px; margin-left: 40px; margin-top: 2px; }
  .address {
    position: absolute; right: 34px; bottom: 56px; width: 210px;
    text-align: center; color: var(--white);
    font-size: 14px; line-height: 1.4;
  }
  .address svg { display: block; margin: 0 auto 8px; }
</style>
</head>
<body>

<section class="card card-front" aria-label="Card front">
  <div class="front-brand">
    <span class="brand-dot"></span>
    <span class="brand-name">MORVEK</span>
  </div>
  <p class="front-web">www.morveklab.org</p>
</section>

<section class="card card-back" aria-label="Card back">
  <svg class="back-panel" width="620" height="354" viewBox="0 0 620 354">
    <polygon points="330,0 620,0 620,354 410,354" fill="var(--red)"/>
    <polygon points="318,96 352,96 352,118" fill="var(--blue-dark)"/>
  </svg>

  <div class="back-brand">
    <div class="back-brand-row">
      <span class="brand-dot"></span>
      <span class="brand-name">MORVEK</span>
    </div>
    <p class="lab-name">Microbial Dose-Response/Exposure<br>Bridging Studies Laboratory</p>
  </div>

  <ul class="contact-list">
    <li>
      <span class="contact-icon">
        <svg width="14" height="14" viewBox="0 0 24 24"><path fill="#fff" d="M6.6 10.8a15 15 0 0 0 6.6 6.6l2.2-2.2a1 1 0 0 1 1-.25 11.4 11.4 0 0 0 3.6.57 1 1 0 0 1 1 1V20a1 1 0 0 1-1 1A17 17 0 0 1 3 4a1 1 0 0 1 1-1h3.5a1 1 0 0 1 1 1c0 1.25.2 2.45.57 3.57a1 1 0 0 1-.25 1z"/></svg>
      </span>816-555-0142
    </li>
    <li>
      <span class="contact-icon">
        <svg width="12" height="14" viewBox="0 0 12 16"><rect x="1.5" y="1" width="9" height="14" rx="1.5" fill="none" stroke="#fff" stroke-width="1.5"/><circle cx="6" cy="12.5" r="0.9" fill="#fff"/></svg>
      </span>816-555-0187
    </li>
    <li>
      <span class="contact-icon">
        <svg width="14" height="10" viewBox="0 0 16 11"><rect x="0.75" y="0.75" width="14.5" height="9.5" fill="none" stroke="#fff" stroke-width="1.5"/><path d="M1 1l7 5.5L15 1M1 10l5-4.5M15 10l-5-4.5" fill="none" stroke="#fff" stroke-width="1.3"/></svg>
      </span>hello@morveklab.org
    </li>
    <li>
      <span class="contact-icon">
        <svg width="14" height="14" viewBox="0 0 16 16"><circle cx="8" cy="8" r="6.5" fill="none" stroke="#fff" stroke-width="1.4"/><path d="M1.5 8h13M8 1.5c-3 3.5-3 9.5 0 13M8 1.5c3 3.5 3 9.5 0 13" fill="none" stroke="#fff" stroke-width="1.1"/></svg>
      </span>www.morveklab.org
    </li>
  </ul>

  <div class="name-ribbon">
    <span class="person-name">Ravi Tembhare</span>
    <span class="person-role">Director</span>
  </div>

  <div class="address">
    <svg width="14" height="18" viewBox="0 0 14 18"><path fill="#fff" d="M7 0a7 7 0 0 0-7 7c0 5 7 11 7 11s7-6 7-11a7 7 0 0 0-7-7zm0 9.5A2.5 2.5 0 1 1 7 4.5a2.5 2.5 0 0 1 0 5z"/></svg>
    Halden House, West Bottoms<br>Unit 12, Genessee Road
  </div>
</section>

</body>
</html>
```